50 plus

Full Color 1/8 page newspaper ad . We are 1 stop shop for all mobility needs. Highlight Accessible Van Rentals & Sales. 50 free miles on your rental when you mention this ad.

```html
<!DOCTYPE html>
<html lang="en">
<head>
<meta charset="utf-8">
<title>Summit Ride Access &amp; Mobility – Accessible Vans</title>
<link rel="stylesheet" href="https://fonts.googleapis.com/css2?family=Fredoka:wght@500;600&family=Montserrat:wght@300;700&family=Quicksand:wght@400;500&display=swap">
<style>
  :root{
    --navy:#29205f;
    --white:#ffffff;
    --ink:#1d1a3a;
    --van-light:#e9eaee;
    --van-mid:#a9adb6;
    --gear-light:#eeeeee;
    --gear-dark:#6a6a74;
  }
  *{margin:0;padding:0;box-sizing:border-box}
  html,body{width:1200px;height:811px;overflow:hidden;background:var(--white)}
  .ad{position:relative;width:1200px;height:811px;background:var(--white);overflow:hidden;font-family:"Quicksand",sans-serif;color:var(--ink)}
  .top-band{position:absolute;left:0;top:0;width:1200px;height:207px;background:var(--navy)}
  .headline{position:absolute;z-index:3;left:28px;top:18px;font-family:"Fredoka",sans-serif;font-weight:600;font-size:76px;line-height:82px;color:var(--white);letter-spacing:0.5px}
  .brand-box{position:absolute;z-index:3;left:833px;top:3px;width:326px;height:140px;background:var(--white);display:flex;flex-direction:column;align-items:center;justify-content:center;gap:10px}
  .brand-name{width:288px;padding:10px 0;background:var(--navy);color:var(--white);font-family:"Fredoka",sans-serif;font-weight:600;font-size:25px;line-height:28px;text-align:center}
  .brand-url{font-family:"Montserrat",sans-serif;font-weight:700;font-size:15px;letter-spacing:1.5px;color:var(--ink)}
  .van-photo{position:absolute;z-index:1;left:520px;top:100px;width:645px;height:318px;border-radius:40px 120px 60px 20px;background:radial-gradient(ellipse at 60% 50%,var(--van-light),var(--van-mid) 80%,rgba(169,173,182,0) 100%)}
  .promo-badge{position:absolute;z-index:2;left:642px;top:292px;width:140px;height:140px}
  .offer{position:absolute;left:24px;top:216px;color:var(--navy);font-family:"Montserrat",sans-serif;font-size:48px;line-height:50px;letter-spacing:-0.5px}
  .offer b{font-weight:700}
  .offer span{font-weight:300}
  .pitch{position:absolute;left:24px;top:424px;width:472px;font-size:22.5px;line-height:31px;color:var(--ink)}
  .contact{position:absolute;left:24px;top:656px;display:flex;align-items:center;gap:12px}
  .contact-label{font-family:"Montserrat",sans-serif;font-weight:700;font-size:16px;line-height:23px;color:var(--ink)}
  .contact-phones{font-family:"Fredoka",sans-serif;font-weight:600;font-size:40px;line-height:43px;color:var(--ink)}
  .range-title{position:absolute;z-index:2;left:602px;top:442px;font-family:"Fredoka",sans-serif;font-weight:600;font-size:28px;line-height:36px;color:var(--navy)}
  .product{position:absolute;top:488px;width:170px;text-align:center}
  .product-photo{height:192px;margin:0 auto;width:150px;border-radius:20px;background:radial-gradient(ellipse at 50% 50%,var(--gear-dark),var(--gear-light) 75%,var(--white) 100%)}
  .product-name{margin-top:10px;font-family:"Montserrat",sans-serif;font-weight:700;font-size:19px;line-height:24px;color:var(--navy)}
  .tagline{position:absolute;left:0;top:748px;width:1200px;height:63px;background:var(--navy);padding:4px}
  .tagline-inner{height:100%;border:2px solid var(--white);border-bottom:none;display:flex;align-items:center;justify-content:center;color:var(--white);font-family:"Montserrat",sans-serif;font-weight:700;font-size:28px;letter-spacing:9.6px;white-space:nowrap}
</style>
</head>
<body>
<main class="ad">
  <div class="top-band"></div>

  <div class="van-photo" role="img" aria-label="Silver wheelchair-accessible minivan with side ramp deployed and a smiling man in a power wheelchair beside it"></div>

  <h1 class="headline">Let’s Maximize<br>Your Mobility!</h1>

  <div class="brand-box">
    <div class="brand-name">SUMMIT RIDE<br>ACCESS &amp; MOBILITY</div>
    <div class="brand-url">www.summitrideaccess.com</div>
  </div>

  <svg class="promo-badge" viewBox="0 0 140 140" aria-label="50 free miles on your rental when you mention this ad">
    <polygon fill="#29205f" points="70,2 78,14 90,5 94,19 108,14 108,28 122,27 118,41 132,44 124,56 136,64 126,73 135,84 122,89 127,102 113,104 114,118 100,116 97,130 85,124 78,137 70,126 60,137 55,124 41,130 39,116 25,118 27,104 12,102 18,89 4,84 14,73 4,64 16,56 8,44 22,41 18,27 32,28 32,14 46,19 50,5 62,14"/>
    <g transform="rotate(-12 70 70)" fill="#fff" font-family="Fredoka, sans-serif" font-weight="500" font-size="12.5" text-anchor="middle">
      <text x="70" y="48">50 free miles</text>
      <text x="70" y="64">on your rental</text>
      <text x="70" y="80">when you</text>
      <text x="70" y="96">mention this ad</text>
    </g>
  </svg>

  <h2 class="offer"><b>BUY OR RENT</b><br><span>ONE OF OUR WELL<br>MAINTAINED</span><br><b>ACCESSIBLE VANS</b></h2>

  <p class="pitch">We know that travel can be difficult with mobility devices, so that’s why we rent out accessible vans! This is a great opportunity to get a loved one out of the house, or even to a doctor’s appointment! We are committed to making mobility and accessibility a breeze!</p>

  <div class="contact">
    <div class="contact-label">FOR MORE<br>INFORMATION<br>CALL</div>
    <div class="contact-phones">(307) 555-0142<br>(970) 555-0187</div>
  </div>

  <h3 class="range-title">Our Access &amp; Mobility range</h3>

  <div class="product" style="left:476px">
    <div class="product-photo" role="img" aria-label="Red four-wheel mobility scooter with front basket"></div>
    <div class="product-name">MOBILITY<br>SCOOTER</div>
  </div>
  <div class="product" style="left:660px">
    <div class="product-photo" role="img" aria-label="Silver knee scooter with handlebars"></div>
    <div class="product-name">MOBILITY<br>SCOOTER</div>
  </div>
  <div class="product" style="left:828px">
    <div class="product-photo" role="img" aria-label="Blue rolling walker with seat"></div>
    <div class="product-name">WALKING<br>AIDS</div>
  </div>
  <div class="product" style="left:1012px">
    <div class="product-photo" role="img" aria-label="Black and blue power wheelchair"></div>
    <div class="product-name">POWER<br>WHEELCHAIR</div>
  </div>

  <footer class="tagline"><div class="tagline-inner">The one stop shop for all of your mobility needs</div></footer>
</main>
</body>
</html>
```